Banner Ad for website hompage - Design Project

We need 4 banner ads for the homepage of a Rent a Car company based in dubai. We rent a wide range of cars but mainly deal in the affordable cars category. Our website colors are mainly red, white and black and I can send pictures of the website (attached) if you want something to compare possible design ideas with. The banners need to promote different messages and must be appealing to the end user. It must also use pictures of cars that exist in our fleet (Pls note: this is only if you are using cars in the banner ad)

The 4 banner ads needed are as follows:
1) should promote something along the lines of we have 20+ models available and reserve a car now (This banner should also have a reserve now button, not the actual button but it's design. The button will be made and coded by us)
2) should promote something along the lines of we offer personalised service and we look after each and every custoemr individually
3) we provide attractive rates based on daily, weekly, monthly and longer rental periods (should also incorporate a reserve now message)
4) Like us on quorvia and follow us on social media for additional offers and discounts (would like for this to have a like button design implemented in it which will be linked to quorvia.)

Also please not the picture file size is 940pixels by 400pixels

Finally: I also need the psd files for the banners.

```html
<!DOCTYPE html>
<html lang="en">
<head>
<meta charset="utf-8">
<title>Marlow Car Hire – Attractive Rates</title>
<link href="https://fonts.googleapis.com/css2?family=Open+Sans:wght@400;600;700;800&display=swap" rel="stylesheet">
<style>
  :root {
    --red: #e4341a;
    --red-deep: #c92a12;
    --black: #111111;
    --white: #ffffff;
    --nav-grey: #444444;
    --header-top: #ffffff;
    --header-bottom: #ececec;
    --page-bg: #f4f4f4;
  }
  * { margin: 0; padding: 0; box-sizing: border-box; }
  html, body {
    width: 1200px; height: 663px; overflow: hidden;
    background: var(--page-bg);
    font-family: "Open Sans", Arial, sans-serif;
  }
  .site { position: relative; width: 1200px; height: 663px; }

  .site-header {
    position: absolute; left: 0; top: 0; width: 1200px; height: 145px;
    background: linear-gradient(var(--header-top), var(--header-bottom));
  }
  .brand {
    position: absolute; left: 62px; top: 50px;
    display: flex; align-items: center; gap: 10px;
    font-weight: 700; font-size: 30px; color: var(--red);
  }
  .brand-dot { width: 18px; height: 18px; border-radius: 50%; background: var(--red); }
  .main-nav {
    position: absolute; right: 96px; top: 70px;
    display: flex; gap: 25px; list-style: none;
  }
  .main-nav li {
    font-weight: 700; font-size: 18px; color: var(--nav-grey);
    padding-bottom: 4px; letter-spacing: -0.2px;
  }
  .main-nav li.is-active { color: var(--red); border-bottom: 2px solid var(--red); }

  .hero { position: absolute; left: 0; top: 145px; width: 1200px; height: 489px; }
  .hero-art { position: absolute; inset: 0; }

  .hero-tag {
    position: absolute; left: 62px; top: 105px; height: 52px; padding: 0 19px;
    background: var(--black); color: var(--white);
    font-weight: 700; font-size: 21px; line-height: 52px;
  }
  .hero-tag::after {
    content: ""; position: absolute; left: 0; bottom: -12px;
    border-top: 12px solid var(--black); border-right: 12px solid transparent;
  }
  .hero-title {
    position: absolute; left: 62px; top: 175px;
    color: var(--white); font-weight: 800; font-size: 61px; line-height: 1;
    letter-spacing: -0.5px; white-space: nowrap;
    text-shadow: 0 2px 3px rgba(0,0,0,.25);
  }
  .hero-periods {
    position: absolute; left: 62px; top: 242px;
    color: var(--white); font-weight: 700; font-size: 29px; line-height: 34px;
    white-space: nowrap;
    text-shadow: 0 1px 2px rgba(0,0,0,.25);
  }
  .period { color: var(--black); font-weight: 600; font-size: 31px; text-shadow: none; }
  .period-sep {
    display: inline-block; width: 1px; height: 28px; margin: 0 9px;
    background: rgba(0,0,0,.25); vertical-align: -4px;
  }

  .reserve-btn {
    position: absolute; left: 62px; top: 342px; width: 310px; height: 70px;
    border-radius: 35px; background: var(--black);
    border: 3px solid var(--white);
    color: var(--white); font-size: 24px; font-weight: 400; letter-spacing: -0.3px;
    padding-left: 90px; line-height: 64px;
  }
  .reserve-avatar {
    position: absolute; left: -3px; top: -6px; width: 76px; height: 76px;
    border-radius: 50%; border: 3px solid var(--white);
    background: linear-gradient(160deg, #f3ece6, #cfc3b8);
  }

  .slider-arrow {
    position: absolute; top: 240px; width: 40px; height: 48px;
  }
  .slider-arrow.prev { left: 8px; }
  .slider-arrow.next { left: 1124px; }

  .hero-shadow {
    position: absolute; left: 40px; top: 634px; width: 1120px; height: 20px;
    background: radial-gradient(ellipse at top, rgba(0,0,0,.25), transparent 70%);
  }
</style>
</head>
<body>
<div class="site">
  <header class="site-header">
    <div class="brand"><span class="brand-dot"></span>Marlow Car Hire</div>
    <ul class="main-nav">
      <li>HOME</li>
      <li class="is-active">ABOUT US</li>
      <li>SERVICES &amp; BENEFITS</li>
      <li>BLOG</li>
      <li>CONTACT US</li>
      <li>RESOURCES</li>
    </ul>
  </header>

  <section class="hero">
    <svg class="hero-art" width="1200" height="489" viewBox="0 0 1200 489">
      <defs>
        <linearGradient id="photoTone" x1="0" y1="0" x2="1" y2="1">
          <stop offset="0" stop-color="#c9d3de"/>
          <stop offset="0.45" stop-color="#a9b7c7"/>
          <stop offset="1" stop-color="#4d6a92"/>
        </linearGradient>
        <linearGradient id="redPanel" x1="0" y1="0" x2="0" y2="1">
          <stop offset="0" stop-color="#e8391c"/>
          <stop offset="1" stop-color="#c92a12"/>
        </linearGradient>
      </defs>
      <rect x="480" y="0" width="720" height="489" fill="url(#photoTone)" role="img" aria-label="Hand holding car keys in front of a lot of parked blue cars"/>
      <polygon points="0,0 706,0 484,489 0,489" fill="#ffffff"/>
      <polygon points="0,0 700,0 478,489 0,489" fill="url(#redPanel)"/>
      <polygon points="508,350 565,350 555,372 498,372" fill="#ffffff"/>
      <circle cx="519" cy="361" r="4.5" fill="#c92a12"/>
      <circle cx="530" cy="361" r="4.5" fill="#c92a12"/>
      <circle cx="541" cy="361" r="4.5" fill="#111111"/>
      <circle cx="552" cy="361" r="4.5" fill="#c92a12"/>
    </svg>

    <div class="hero-tag">we provide</div>
    <div class="hero-title">Attractive Rates</div>
    <div class="hero-periods">
      based on <span class="period">Daily</span><span class="period-sep"></span><span class="period">Weekly</span><span class="period-sep"></span><span class="period">Monthly</span><br>
      and longer rental periods
    </div>

    <div class="reserve-btn">
      <span class="reserve-avatar" role="img" aria-label="Portrait of a friendly rental agent"></span>
      RESERVE NOW
    </div>

    <svg class="slider-arrow prev" viewBox="0 0 40 48" aria-label="Previous slide">
      <circle cx="20" cy="24" r="18" fill="none" stroke="rgba(255,255,255,.6)" stroke-width="2"/>
      <path d="M23 16 L15 24 L23 32" fill="none" stroke="rgba(255,255,255,.7)" stroke-width="2.5"/>
    </svg>
    <svg class="slider-arrow next" viewBox="0 0 40 48" aria-label="Next slide">
      <circle cx="20" cy="24" r="18" fill="none" stroke="rgba(255,255,255,.6)" stroke-width="2"/>
      <path d="M17 16 L25 24 L17 32" fill="none" stroke="rgba(255,255,255,.7)" stroke-width="2.5"/>
    </svg>
  </section>
  <div class="hero-shadow"></div>
</div>
</body>
</html>
```